KR TMW PowerPoint Template Design

Looking for an eye catching and clean powerpoint template to deliver sales proposals to our clients. KR TMW is a sales and marketing representation business in the hospitality industry, Logo it attached.

```html
<!DOCTYPE html>
<html lang="en">
<head>
<meta charset="UTF-8">
<title>KR TMW – Presentation Title</title>
<link rel="stylesheet" href="https://fonts.googleapis.com/css2?family=Lato:wght@400;700&display=swap">
<style>
  :root {
    --brand-bronze: #7d6a3e;
    --paper: #ffffff;
    --footer-grey: #808080;
    --text-light: #ffffff;
  }
  html, body {
    margin: 0;
    padding: 0;
    width: 1200px;
    height: 900px;
    overflow: hidden;
    background: var(--paper);
  }
  .slide {
    position: relative;
    width: 1200px;
    height: 900px;
    font-family: "Lato", sans-serif;
  }
  .hero {
    position: absolute;
    top: 0;
    left: 0;
    width: 1200px;
    height: 592px;
    background: var(--brand-bronze);
  }
  .hero-title {
    position: absolute;
    top: 290px;
    left: 0;
    width: 100%;
    margin: 0;
    text-align: center;
    color: var(--text-light);
    font-weight: 700;
    font-size: 51px;
    letter-spacing: 1px;
    line-height: 1;
  }
  .hero-subtitle {
    position: absolute;
    top: 370px;
    left: 0;
    width: 100%;
    margin: 0;
    text-align: center;
    color: var(--text-light);
    font-weight: 400;
    font-size: 33px;
    line-height: 1;
  }
  .brand {
    position: absolute;
    top: 592px;
    left: 0;
    width: 1200px;
    height: 278px;
    display: flex;
    align-items: center;
    justify-content: center;
  }
  .brand-name {
    color: var(--brand-bronze);
    font-weight: 700;
    font-size: 64px;
    letter-spacing: 4px;
  }
  .footer-band {
    position: absolute;
    bottom: 0;
    left: 0;
    width: 1200px;
    height: 30px;
    background: var(--footer-grey);
  }
</style>
</head>
<body>
  <main class="slide">
    <section class="hero">
      <h1 class="hero-title">PERSENTATION TITLE HERE</h1>
      <p class="hero-subtitle">Subtext here</p>
    </section>
    <section class="brand">
      <span class="brand-name">KR TMW</span>
    </section>
    <div class="footer-band"></div>
  </main>
</body>
</html>
```